Jolie Plume Gourmet Brie Packaging

I developed and market a 10oz wheel (7inch dia) and a 6 oz wheel (5 inch dia) Gourmet Brie Cheese Line. They are all double cream bries, topped with decadent concoctions and wrapped with buttery puff pastry. They are frozen and vacuum sealed. They are sold in markets as a frozen item. I am looking for a paper "slip"/ wrap to house the brie that would have my logo, nutritional info, and cooking instructions in a mod fresh background. The company Name is Jolie Plume (bright spoon). and the Product if Gourmet Brie. I would like to wrapper to be able to house both sizes so I dont double my costs. My Logo for Jolie Plume is a Red sketched chicken in the middle of the name. The writing is in Black (le Carte pen is the font I used)
My website is brightspoon-events.example.
Updates

I have added a logo file for the packaging.  The logo should be the jolie plume chicken and not bright spoon events.  Also, I would like the style and colors to match with this  - THANKS!

I have updated to Jolie Plume Logo - Please make the change to your designs.  I will be selecting design a week from today.  The choosen design may require a few edits, but minimal. Thanks!

Reason: I will be choosing Design April 2. Please have any changes, designs and or ideas to Jolie Plume by then. Thanks you all so much for what you submitted....I like them all!!!!

Target Market(s)

Gourmet Food/Wine Shops /upscale grocery.

Industry/Entity Type

Cooking

Requirements
Must have
• Ingredients, Nutritional info, directions.
Logo and name.

```html
<!DOCTYPE html>
<html lang="en">
<head>
<meta charset="utf-8">
<title>Jolie Plume Gourmet Brie Packaging</title>
<link href="https://fonts.googleapis.com/css2?family=Rye&display=swap" rel="stylesheet">
<style>
  :root {
    --page: #b9bab9;
    --board: #e9eaec;
    --board-light: #f4f4f5;
    --slate: #4e4c4d;
    --red: #d64027;
    --blue: #1f6fa8;
    --pink: #c2266f;
    --ink: #3a3a3a;
    --white: #ffffff;
    --cream: #f6ecd6;
    --pattern-red: #fbf1ef;
    --pattern-blue: #f3ead6;
    --frame-silver: #d3d4d6;
    --grey-field: #dcdbd9;
    --beige-field: #e8cfa6;
    --pastry-light: #f3c46a;
    --pastry-dark: #c98a2e;
    --strip: #c6c7c8;
  }
  html, body {
    margin: 0;
    padding: 0;
    width: 1169px;
    height: 1200px;
    overflow: hidden;
    background: var(--page);
  }
  .canvas {
    position: relative;
    width: 1169px;
    height: 1200px;
  }
  .board {
    position: absolute;
    left: 13px;
    top: 13px;
    width: 1144px;
    height: 1133px;
    border-radius: 44px 44px 0 0;
    background: radial-gradient(ellipse at 50% 30%, var(--board-light), var(--board) 70%);
  }
  .caption-strip {
    position: absolute;
    left: 13px;
    top: 1140px;
    width: 1144px;
    height: 50px;
    background: linear-gradient(var(--strip), #dedfe0 50%, var(--strip));
  }
  .artwork {
    position: absolute;
    left: 0;
    top: 0;
  }
  .brand-name {
    font-family: "Rye", serif;
    fill: var(--pink);
  }
  .brand-tag {
    font-family: "Rye", serif;
    fill: var(--ink);
    letter-spacing: 1px;
  }
  .product-name {
    font-family: "Rye", serif;
    fill: var(--white);
  }
</style>
</head>
<body>
<div class="canvas">
  <div class="board"></div>
  <div class="caption-strip"></div>

  <svg class="artwork" width="1169" height="1200" viewBox="0 0 1169 1200" xmlns="http://www.w3.org/2000/svg">
    <defs>
      <filter id="drop" x="-10%" y="-10%" width="130%" height="130%">
        <feDropShadow dx="5" dy="6" stdDeviation="5" flood-color="#000" flood-opacity="0.35"/>
      </filter>
      <radialGradient id="pastry" cx="50%" cy="45%" r="55%">
        <stop offset="0%" stop-color="var(--pastry-light)"/>
        <stop offset="75%" stop-color="#e8ad4e"/>
        <stop offset="100%" stop-color="var(--pastry-dark)"/>
      </radialGradient>
      <linearGradient id="silver" x1="0" y1="0" x2="1" y2="1">
        <stop offset="0%" stop-color="#f2f2f3"/>
        <stop offset="50%" stop-color="var(--frame-silver)"/>
        <stop offset="100%" stop-color="#f5f5f6"/>
      </linearGradient>
      <clipPath id="upper-small-left"><rect x="150" y="192" width="318" height="164"/></clipPath>
      <clipPath id="upper-small-right"><rect x="707" y="192" width="318" height="164"/></clipPath>
      <clipPath id="upper-large-left"><rect x="98" y="560" width="420" height="285"/></clipPath>
      <clipPath id="upper-large-right"><rect x="640" y="560" width="420" height="285"/></clipPath>
    </defs>

    <!-- Small label, red -->
    <g class="label-swatch label-swatch--red">
      <rect x="150" y="192" width="318" height="268" rx="12" fill="var(--slate)" filter="url(#drop)"/>
      <circle cx="308" cy="327" r="93" fill="none" stroke="var(--white)" stroke-width="3"/>
      <circle cx="308" cy="327" r="96" fill="var(--pattern-red)" clip-path="url(#upper-small-left)" role="img" aria-label="Fine swirl pattern in pale red"/>
      <circle cx="308" cy="327" r="100" fill="none" stroke="var(--red)" stroke-width="7"/>
      <text class="brand-name" x="306" y="265" font-size="11" text-anchor="middle">Bright Spoon</text>
      <text class="brand-tag" x="306" y="274" font-size="5" text-anchor="middle">EVENTS</text>
      <rect x="178" y="300" width="256" height="56" fill="var(--white)"/>
      <rect x="195" y="312" width="222" height="33" fill="var(--red)"/>
      <text class="product-name" x="306" y="336" font-size="20" text-anchor="middle">GOURMET BRIE</text>
    </g>

    <!-- Small label, blue -->
    <g class="label-swatch label-swatch--blue">
      <rect x="707" y="192" width="318" height="268" rx="12" fill="var(--slate)" filter="url(#drop)"/>
      <circle cx="865" cy="327" r="93" fill="none" stroke="var(--white)" stroke-width="3"/>
      <circle cx="865" cy="327" r="96" fill="var(--pattern-blue)" clip-path="url(#upper-small-right)" role="img" aria-label="Fine swirl pattern in warm cream"/>
      <circle cx="865" cy="327" r="100" fill="none" stroke="var(--blue)" stroke-width="7"/>
      <rect x="743" y="300" width="244" height="56" fill="var(--cream)"/>
      <rect x="760" y="312" width="222" height="33" fill="var(--blue)"/>
      <text class="product-name" x="871" y="336" font-size="20" text-anchor="middle">GOURMET BRIE</text>
    </g>

    <!-- Large wrap, red on grey -->
    <g class="wrap wrap--red">
      <rect x="98" y="565" width="417" height="417" fill="url(#silver)" filter="url(#drop)"/>
      <rect x="111" y="578" width="393" height="393" fill="var(--grey-field)"/>
      <circle cx="308" cy="775" r="191" fill="url(#pastry)" role="img" aria-label="Photo of a golden puff pastry wrapped brie wheel"/>
      <circle cx="306" cy="773" r="157" fill="var(--pattern-red)" clip-path="url(#upper-large-left)" role="img" aria-label="Fine swirl pattern in pale red"/>
      <circle cx="306" cy="773" r="161" fill="none" stroke="var(--red)" stroke-width="10"/>
      <text class="brand-name" x="300" y="680" font-size="18" text-anchor="middle">Bright Spoon</text>
      <text class="brand-tag" x="300" y="694" font-size="7" text-anchor="middle">EVENTS</text>
      <rect x="117" y="735" width="389" height="82" fill="var(--white)"/>
      <rect x="137" y="746" width="343" height="60" fill="var(--red)" stroke="var(--white)" stroke-width="2"/>
      <text class="product-name" x="308" y="787" font-size="33" text-anchor="middle">GOURMET BRIE</text>
    </g>

    <!-- Large wrap, blue on beige -->
    <g class="wrap wrap--blue">
      <rect x="640" y="560" width="417" height="428" fill="url(#silver)" filter="url(#drop)"/>
      <rect x="653" y="578" width="393" height="395" fill="var(--beige-field)"/>
      <circle cx="851" cy="775" r="191" fill="url(#pastry)" role="img" aria-label="Photo of a golden puff pastry wrapped brie wheel"/>
      <circle cx="851" cy="773" r="157" fill="var(--pattern-blue)" clip-path="url(#upper-large-right)" role="img" aria-label="Fine swirl pattern in warm cream"/>
      <circle cx="851" cy="773" r="161" fill="none" stroke="var(--blue)" stroke-width="10"/>
      <text class="brand-name" x="847" y="680" font-size="18" text-anchor="middle">Bright Spoon</text>
      <text class="brand-tag" x="847" y="694" font-size="7" text-anchor="middle">EVENTS</text>
      <rect x="667" y="735" width="379" height="82" fill="var(--cream)"/>
      <rect x="678" y="746" width="343" height="60" fill="var(--blue)" stroke="var(--white)" stroke-width="2"/>
      <text class="product-name" x="850" y="787" font-size="33" text-anchor="middle">GOURMET BRIE</text>
    </g>
  </svg>
</div>
</body>
</html>
```